Change the world and help build SpinLOOM.tv!

We need a mobile website design for our Beta release - see wireframes attached.
See our Logo design files attached along with fonts, etc.
Please see enclosed .PDF that provides a great overview of our company, LOOM.
Any questions, feel free to ask - we're very engaged here on Sketch Hive and will make ourselves available.
Thanks!
Tobias
Updates
Very pleased with what's coming in! Would like to see some more variety and more volume of designs.
Target Market(s)
Ages 13+ (all genders, races, creeds, income levels, etc)
Coding
Coded - Design and coding required
Number of Pages Required
5+ page
Font styles to use
Colors
Designer to choose colors to be used in the design.
Look and feel
Each slider illustrates characteristics of the customer's brand and the style your logo design should communicate.

```html
<!DOCTYPE html>
<html lang="en">
<head>
<meta charset="utf-8">
<title>SpinLOOM.tv – Mobile Beta Screens</title>
<link rel="stylesheet" href="https://fonts.googleapis.com/css2?family=Open+Sans:wght@400;600;700;800&display=swap">
<style>
  :root{
    --navy:#1e2f5c;
    --navy-dark:#14203f;
    --ink:#1c2230;
    --muted:#6b7280;
    --line:#d5d9e0;
    --panel:#f1f3f6;
    --white:#ffffff;
    --footer:#1b1e28;
    --canvas:#ffffff;
  }
  *{box-sizing:border-box;margin:0;padding:0}
  html,body{width:1200px;height:2500px;overflow:hidden;background:var(--canvas);
    font-family:"Open Sans",Arial,sans-serif;color:var(--ink)}
  .canvas{position:relative;width:1200px;height:2500px}

  .screen{position:absolute;width:320px;background:var(--white);
    box-shadow:0 6px 24px rgba(20,32,63,.14);display:flex;flex-direction:column;overflow:hidden}
  .screen--home{left:60px;top:200px}
  .screen--signup{left:440px;top:200px}
  .screen--thanks{left:820px;top:200px}
  .screen--influencer{left:440px;top:1020px}
  .screen--thanks-influencer{left:820px;top:1020px}

  .app-header{height:64px;display:flex;align-items:center;justify-content:center;position:relative;
    border-bottom:1px solid var(--line);background:var(--white)}
  .brand{display:flex;align-items:center;gap:8px;font-weight:800;font-size:20px;color:var(--navy);letter-spacing:.5px}
  .brand-mark{width:14px;height:14px;background:var(--navy)}
  .back{position:absolute;left:16px;top:22px}

  .nav-buttons{display:flex;justify-content:space-between;padding:12px 16px}
  .btn{background:var(--navy);color:var(--white);font-size:11px;font-weight:600;border:none;
    padding:7px 14px;border-radius:3px;text-align:center}
  .btn--wide{display:block;margin:0 auto;padding:9px 22px;font-size:11px}

  .body{padding:16px 18px;flex:1;background:var(--panel)}
  .body--home{background:var(--white);padding:16px 0 22px}
  .lead{font-weight:700;font-size:15px;line-height:1.35;padding:0 18px 18px;color:var(--ink)}
  .photo{height:200px;margin-bottom:22px;
    background:linear-gradient(135deg,#7fa7b3 0%,#c9b8b0 45%,#d6909a 75%,#4f6c80 100%)}

  .intro{font-size:12px;line-height:1.5;margin-bottom:14px;color:var(--ink)}
  .form-card{background:var(--white);padding:14px 14px 18px;box-shadow:0 1px 4px rgba(0,0,0,.06)}
  .field{margin-bottom:10px}
  .field label{display:block;font-size:9.5px;color:var(--muted);margin-bottom:4px}
  .input{height:26px;border:1px solid var(--line);border-radius:2px;background:var(--white);position:relative}
  .input--select svg{position:absolute;right:8px;top:9px}
  .textarea{height:60px;border:1px solid var(--line);border-radius:2px}
  .textarea--filled{height:120px;padding:6px 7px;font-size:8.5px;line-height:1.45;color:#9aa0ab}
  .form-card .btn--wide{margin-top:14px}

  .thanks-card{background:var(--white);padding:20px 18px 24px;box-shadow:0 1px 4px rgba(0,0,0,.08)}
  .thanks-card h2{font-size:15px;font-weight:700;text-align:center;margin-bottom:14px;color:var(--ink)}
  .thanks-card p{font-size:10px;line-height:1.55;color:var(--ink);margin-bottom:10px}
  .sign{font-size:10px;line-height:1.5}
  .sign strong{font-weight:700}

  .app-footer{background:var(--footer);color:var(--white);font-size:10.5px;padding:12px 16px;
    display:grid;grid-template-columns:1fr auto;row-gap:10px}
</style>
</head>
<body>
<main class="canvas">

  <section class="screen screen--home" aria-label="Home screen">
    <header class="app-header"><div class="brand"><span class="brand-mark"></span>SpinLOOM.tv</div></header>
    <div class="nav-buttons"><span class="btn">Join Beta</span><span class="btn">Influencer Sign up</span></div>
    <div class="body body--home">
      <p class="lead">LOOM is an innovative game that will disrupt the 300 year old delivery model for the treatment of anxiety and depression</p>
      <div class="photo" role="img" aria-label="Photo of a young woman smiling at her desk in front of a screen"></div>
      <span class="btn btn--wide" style="width:240px">Donate to our FundNest campaign</span>
    </div>
    <footer class="app-footer"><span>Terms &amp; Conditions</span><span>Privacy policy</span><span>About LOOM</span><span>The LOOM Team</span></footer>
  </section>

  <section class="screen screen--signup" aria-label="Beta sign up screen">
    <header class="app-header">
      <svg class="back" width="20" height="20" viewBox="0 0 20 20"><path d="M17 10H4M9 4l-6 6 6 6" fill="none" stroke="#1c2230" stroke-width="2"/></svg>
      <div class="brand"><span class="brand-mark"></span>SpinLOOM.tv</div>
    </header>
    <div class="body">
      <p class="intro">Sign up to receive an invitation to join our pre-launch Beta version of LOOM! Join our growing community of mental health warriors and help build a platform that can improve the lives of millions of people.</p>
      <div class="form-card">
        <div class="field"><label>Name</label><div class="input"></div></div>
        <div class="field"><label>Email Id</label><div class="input"></div></div>
        <div class="field"><label>Phone</label><div class="input"></div></div>
        <div class="field"><label>Date of Birth</label><div class="input input--select"><svg width="10" height="6" viewBox="0 0 10 6"><path d="M1 1l4 4 4-4" fill="none" stroke="#6b7280" stroke-width="1.4"/></svg></div></div>
        <div class="field"><label>Address</label><div class="input"></div></div>
        <div class="field"><label>Share your story with us</label><div class="textarea"></div></div>
        <span class="btn btn--wide" style="width:120px">Register</span>
      </div>
    </div>
    <footer class="app-footer"><span>Terms &amp; Conditions</span><span>Privacy policy</span><span>About LOOM</span><span>The LOOM Team</span></footer>
  </section>

  <section class="screen screen--thanks" aria-label="Sign up confirmation screen">
    <header class="app-header"><div class="brand"><span class="brand-mark"></span>SpinLOOM.tv</div></header>
    <div class="body" style="padding:22px 18px 60px">
      <div class="thanks-card">
        <h2>Thank you for signing up!</h2>
        <p>Please check your email for information about how your Beta program will work and when you can expect testing the app.</p>
        <p>What a wonderful thank you from the LOOM Team! You're doing a wonderful thing for the world, and we are forever grateful for you!</p>
        <p class="sign">With love,<br><strong>Mara &amp; Co</strong></p>
      </div>
    </div>
  </section>

  <section class="screen screen--influencer" aria-label="Influencer sign up screen">
    <header class="app-header">
      <svg class="back" width="20" height="20" viewBox="0 0 20 20"><path d="M17 10H4M9 4l-6 6 6 6" fill="none" stroke="#1c2230" stroke-width="2"/></svg>
      <div class="brand"><span class="brand-mark"></span>SpinLOOM.tv</div>
    </header>
    <div class="body">
      <p class="intro">As a way of thanking you for joining the LOOM Team, we're giving company stock and ongoing cash bonuses to the first 1,000 people to be accepted into the LOOM Influencer Program.</p>
      <div class="form-card">
        <div class="field"><label>Name</label><div class="input"></div></div>
        <div class="field"><label>Email Id</label><div class="input"></div></div>
        <div class="field"><label>Phone</label><div class="input"></div></div>
        <div class="field"><label>Date of Birth</label><div class="input input--select"><svg width="10" height="6" viewBox="0 0 10 6"><path d="M1 1l4 4 4-4" fill="none" stroke="#6b7280" stroke-width="1.4"/></svg></div></div>
        <div class="field"><label>Address</label><div class="input"></div></div>
        <div class="field"><label>Your Website</label><div class="input"></div></div>
        <div class="field"><label>Share your story with us</label>
          <div class="textarea textarea--filled">Tell us why mental health matters to you, how you reach your audience, which channels you use most, and what kind of content you enjoy creating. A few lines about your community, the people who follow you and the stories you hope to share will help us understand how we can grow together and support each other.</div>
        </div>
        <span class="btn btn--wide" style="width:120px">Register</span>
      </div>
    </div>
    <footer class="app-footer"><span>Terms &amp; Conditions</span><span>Privacy policy</span><span>About LOOM</span><span>The LOOM Team</span></footer>
  </section>

  <section class="screen screen--thanks-influencer" aria-label="Influencer confirmation screen">
    <header class="app-header"><div class="brand"><span class="brand-mark"></span>SpinLOOM.tv</div></header>
    <div class="body" style="padding:22px 18px 60px">
      <div class="thanks-card">
        <h2>Thank you for your interest!</h2>
        <p>Please check your email for information about how our Influencer Program will work and when you can expect hearing from us.</p>
        <p>You're doing a wonderful thing for the world, and we are forever grateful for you!</p>
        <p class="sign">With love,<br><strong>Mara &amp; Co</strong></p>
      </div>
    </div>
  </section>

</main>
</body>
</html>
```